Web site for small printshop

I am looking for a website for small printshop in Iceland, mainly serving university students and artist.

We print posters, flyers, business cards and more.

In addition to our current website, I would like to include design tool, (fx. www.quarlitune.example, www.dravonpix.example or something similar) jobs upload, shopping chart.
Updates

Great work, I am really amazed of the quality of work i am seeing here.

Really way beyond my expectation

GOOD JOB - all of you ! 

Hi all.

The designs submitted have been great, way better than expected.
I really did not expect this level of quality.

Some have been asking me for feedback on their designs, and I will try 
to send some feedback here, without spoiling your creativity.

Likes:
- when the colors of my logo is used in menus, buttons etc.
- simple, not to crowded look.

Dislikes.
- Dark and heavy design
- Lot of text and buttons (crowded look)

Extra info.
- top line (before menus) will contain: Tel - email - language
- menu line will have 5 categories: Home - service - submission of works - FAQ - about us
- 3 large buttons:  Job submit - Job design - ask for offer

LOVE YOUR WORK - great designs so far :)

Target Market(s)

University Students, Artists. Age group 20-30

Industry/Entity Type

University

Requirements
Must have
• The website must be easy to use, clean looking.

```html
<!DOCTYPE html>
<html lang="en">
<head>
<meta charset="utf-8">
<title>VÍKURPRENT – Printing service</title>
<link href="https://fonts.googleapis.com/css2?family=Open+Sans:wght@400;600;700&family=Arimo:wght@400;700&display=swap" rel="stylesheet">
<style>
:root{
  --red:#e8322c;
  --red-dark:#c81f1a;
  --green:#1f6b3a;
  --green-bright:#8ccf3a;
  --teal-dark:#0c3d34;
  --teal:#16594a;
  --yellow:#f6dc2a;
  --yellow-light:#fdf6a8;
  --yellow-edge:#d9b90e;
  --ink:#333;
  --text:#666;
  --rule:#d6d6d6;
  --heading-bg:#ebebeb;
}
*{box-sizing:border-box;margin:0;padding:0}
html,body{width:1143px;height:1200px;overflow:hidden}
body{position:relative;font-family:Arimo,Arial,sans-serif;color:var(--text);background:linear-gradient(#f3f3f3 0,#fff 120px,#fff 100%)}
a{color:inherit;text-decoration:none}
ul{list-style:none}

/* top bar */
.topbar{position:absolute;left:651px;top:0;width:374px;height:40px;border:1px solid #d3d3d3;border-top:0;border-radius:0 0 10px 10px;background:linear-gradient(#fff,#efefef);display:flex;align-items:center;padding:0 14px 0 16px;gap:10px;font-size:13px}
.lang{display:flex;align-items:center;gap:6px;color:#333;padding-right:10px}
.lang .flag{width:16px;height:11px;background:#2b4a9a;border:1px solid #999}
.account a{color:var(--red)}
.account span{color:var(--red);margin:0 4px}
.phone{display:flex;align-items:center;gap:6px;color:var(--green);font-family:"Open Sans",sans-serif;font-weight:700;font-size:16px}

/* brand */
.brand{position:absolute;left:95px;top:41px;display:flex;align-items:center;gap:10px}
.brand .mark{width:35px;height:45px;background:var(--red);border-radius:2px}
.brand .name{font-family:"Open Sans",sans-serif;font-weight:700;font-size:27px;color:#2f2f2f;letter-spacing:.3px}

/* nav */
.mainnav{position:absolute;left:533px;top:80px;display:flex;align-items:center;font-size:16px;color:#333}
.mainnav li{padding:0 15px;border-left:1px solid #bdbdbd;line-height:20px}
.mainnav li:first-child{border:0;padding:0 10px 0 0}
.mainnav .active{display:block;width:80px;height:29px;line-height:29px;text-align:center;color:#fff;font-weight:700;border-radius:5px;background:linear-gradient(#f26a5f,var(--red-dark))}

/* hero */
.hero{position:absolute;left:95px;top:128px;width:953px;height:367px;background:radial-gradient(ellipse at 55% 70%,#3fb37a 0,#1d8a63 40%,#0f5a4a 75%,#0a3f38 100%);overflow:hidden}
.hero-title{position:absolute;left:25px;top:50px;height:35px;padding:0 14px;background:var(--red);color:#fff;font-family:"Open Sans",sans-serif;font-weight:700;font-size:23px;line-height:35px}
.perks{position:absolute;left:35px;top:107px;color:#fff;font-family:"Open Sans",sans-serif;font-weight:600;font-size:19px}
.perks li{height:31.5px;display:flex;align-items:center;gap:10px}
.cta{position:absolute;left:29px;top:284px;width:131px;height:42px;border-radius:12px;background:linear-gradient(#fff07a,#f1c500);color:#222;font-family:"Open Sans",sans-serif;font-weight:600;font-size:19px;text-align:center;line-height:42px;box-shadow:0 3px 0 #c49c00}
.art-cards{position:absolute;left:368px;top:49px;width:247px;height:244px;border-radius:3px;background:linear-gradient(135deg,#e68ae0,#f28a2e 50%,#1d5fa8)}
.art-brochure{position:absolute;left:628px;top:67px;width:305px;height:228px;border-radius:3px;background:linear-gradient(135deg,#5d5d5d,#c97b4a 40%,#f07c22 70%,#fafafa)}
.dots{position:absolute;left:850px;top:343px;display:flex;gap:9px}
.dots i{width:13px;height:13px;border-radius:50%;background:#fff;box-shadow:0 1px 2px rgba(0,0,0,.4)}
.dots i:first-child{background:var(--green-bright)}

/* steps */
.steps{position:absolute;left:76px;top:495px;width:991px;height:64px;display:flex;background:linear-gradient(var(--yellow),var(--yellow-light));border:1px solid var(--yellow-edge)}
.steps::before,.steps::after{content:"";position:absolute;top:-20px;border-bottom:20px solid #e8c818}
.steps::before{left:-1px;border-left:19px solid transparent}
.steps::after{right:-1px;border-right:19px solid transparent}
.step{display:flex;align-items:center;justify-content:center;gap:22px;border-left:1px solid #e6c92a;font-family:"Open Sans",sans-serif;font-weight:700;font-size:18px;color:#4a4a3a;text-shadow:0 1px 0 #fff}
.step:first-child{border:0}

/* content */
.panel{position:absolute;width:291px}
.panel h2{height:34px;line-height:34px;padding-left:10px;border-left:5px solid var(--red);background:linear-gradient(90deg,var(--heading-bg),#f7f7f7);font-family:"Open Sans",sans-serif;font-size:18px;font-weight:700;color:#222}
.panel h2.green{border-color:var(--green)}
.panel h2.gold{border-color:#f2c500}
.panel h2 em{font-style:normal;color:var(--red)}
.panel p{font-size:12.5px;line-height:19px;margin:10px 10px 0}
.more{display:block;margin:10px 10px 0;font-weight:700;font-size:12px;color:#555}
.twocol{display:grid;grid-template-columns:1fr 1fr;margin:12px 10px 0;font-size:12.5px;line-height:19px}
.twocol li::before,.arrows li::before{content:"";display:inline-block;border-left:4px solid var(--green);border-top:4px solid transparent;border-bottom:4px solid transparent;margin-right:5px}
.editor-shot{margin:7px auto 0;width:217px;height:131px;border:1px solid #bbb;background:linear-gradient(#dfe6ef,#fff 30%,#f4e2d4 60%,#fff);box-shadow:0 2px 4px rgba(0,0,0,.2)}
.arrows{margin:8px 0 0 10px;font-size:12.5px;line-height:25px}
.faq{margin:8px 0 0 0;font-size:12.5px;line-height:25px}
.faq li{display:flex;align-items:center;gap:9px}
.faq li::before{content:"?";width:11px;height:11px;border-radius:50%;background:var(--green);color:#fff;font-size:9px;line-height:11px;text-align:center;font-weight:700}
.quote{margin-top:10px;width:291px;border:3px solid #ddd;border-radius:10px;padding:10px 12px;font-size:12.5px;line-height:19px;background:#fff}
.pager{position:absolute;right:12px;top:9px;display:flex;border:1px solid #bbb;background:#fff}
.pager i{width:12px;height:15px;border-left:1px solid #ccc}
.pager i:first-child{border:0}
.author{margin:28px 0 0 38px;font-size:11px;font-weight:700;font-style:italic;color:var(--green)}
.portrait{position:absolute;left:205px;top:136px;width:80px;height:70px;border:2px solid #bbb;background:linear-gradient(#c9a07c,#e9cdb2)}
.divider{position:absolute;left:129px;top:810px;width:895px;border-top:1px solid #e2e2e2}

/* footer */
.site-footer{position:absolute;left:0;top:1050px;width:1143px;height:150px;background:linear-gradient(var(--teal),var(--teal-dark));color:#fff;font-size:12px}
.fcol{position:absolute;top:10px}
.fcol h3{font-size:14px;font-weight:700;padding-bottom:5px;border-bottom:1px dashed #8fb2a5;margin-bottom:6px}
.fcol li{line-height:23px}
.fsep{position:absolute;top:10px;height:130px;border-left:1px solid #2f7463}
.contact li{display:flex;align-items:center;gap:16px;line-height:23px;margin-bottom:8px}
.social li{display:flex;align-items:center;gap:12px;margin-bottom:17px}
.social i{width:22px;height:22px;border-radius:4px;background:#e6e6e6}
.fbrand{position:absolute;left:815px;top:65px;display:flex;align-items:center;gap:8px;font-family:"Open Sans",sans-serif;font-weight:700;font-size:21px}
.fbrand i{width:28px;height:36px;background:#fff}
.copy{position:absolute;left:903px;top:117px;font-size:12px}
</style>
</head>
<body>

<div class="topbar">
  <span class="lang"><i class="flag"></i>English
    <svg width="12" height="10" viewBox="0 0 12 10"><path d="M2 3l4 4 4-4" fill="none" stroke="#777" stroke-width="2"/></svg></span>
  <span class="account"><a href="#">Register</a><span>|</span><a href="#">Login</a></span>
  <span class="phone">
    <svg width="22" height="22" viewBox="0 0 22 22"><circle cx="11" cy="11" r="10" fill="none" stroke="#1f6b3a" stroke-width="1.6"/><path d="M8 6c-1 1-1 3 1 6s4 4 5 4l1-2-2-1-1 1c-1-.5-2-2-2.5-3l1-1-1-2z" fill="#1f6b3a"/></svg>
    1300 555 019</span>
</div>

<a class="brand" href="#"><i class="mark"></i><span class="name">VÍKURPRENT</span></a>

<nav>
  <ul class="mainnav">
    <li><a class="active" href="#">Home</a></li>
    <li><a href="#">Services &amp; Pricing</a></li>
    <li><a href="#">About Us</a></li>
    <li><a href="#">Info</a></li>
    <li><a href="#">Contact</a></li>
  </ul>
</nav>

<section class="hero">
  <h1 class="hero-title">PRINTING SERVICE WITH:</h1>
  <ul class="perks">
    <li><svg width="16" height="14" viewBox="0 0 16 14"><path d="M1 7l5 5L15 1" fill="none" stroke="#f6dc2a" stroke-width="3"/></svg>Top quality</li>
    <li><svg width="16" height="14" viewBox="0 0 16 14"><path d="M1 7l5 5L15 1" fill="none" stroke="#f6dc2a" stroke-width="3"/></svg>Unbeatable rates</li>
    <li><svg width="16" height="14" viewBox="0 0 16 14"><path d="M1 7l5 5L15 1" fill="none" stroke="#f6dc2a" stroke-width="3"/></svg>Years of experience</li>
    <li><svg width="16" height="14" viewBox="0 0 16 14"><path d="M1 7l5 5L15 1" fill="none" stroke="#f6dc2a" stroke-width="3"/></svg>Personal care</li>
    <li><svg width="16" height="14" viewBox="0 0 16 14"><path d="M1 7l5 5L15 1" fill="none" stroke="#f6dc2a" stroke-width="3"/></svg>Competence and reliability</li>
  </ul>
  <a class="cta" href="#">Try it Now</a>
  <div class="art-cards" role="img" aria-label="Sample printed business cards"></div>
  <div class="art-brochure" role="img" aria-label="Sample printed tri-fold brochure"></div>
  <div class="dots"><i></i><i></i><i></i><i></i></div>
</section>

<div class="steps">
  <div class="step" style="width:218px">
    <svg width="38" height="48" viewBox="0 0 38 48"><path d="M3 3h22l10 10v32H3z" fill="#fdf3a0" stroke="#8a7a10" stroke-width="3" stroke-linejoin="round"/></svg>Your File</div>
  <div class="step" style="width:268px">
    <svg width="50" height="50" viewBox="0 0 50 50"><circle cx="25" cy="25" r="22" fill="#fdf3a0" stroke="#8a7a10" stroke-width="3"/><path d="M25 13l-10 11h6v12h8V24h6z" fill="#f3c400" stroke="#8a7a10" stroke-width="2"/></svg>Upload</div>
  <div class="step" style="width:280px">
    <svg width="50" height="50" viewBox="0 0 50 50"><path d="M4 4h20l8 8v34H4z" fill="#fdf3a0" stroke="#8a7a10" stroke-width="3"/><rect x="10" y="22" width="12" height="10" fill="#8a7a10"/><path d="M13 22v-4a3 3 0 016 0v4" fill="none" stroke="#8a7a10" stroke-width="2"/><path d="M26 44l20-22" stroke="#8a7a10" stroke-width="4"/></svg>Process</div>
  <div class="step" style="width:263px">
    <svg width="50" height="50" viewBox="0 0 50 50"><path d="M2 8h8l6 26h26l5-18H13" fill="#fdf3a0" stroke="#8a7a10" stroke-width="3" stroke-linejoin="round"/><circle cx="19" cy="42" r="4" fill="#8a7a10"/><circle cx="38" cy="42" r="4" fill="#8a7a10"/></svg>Check Out</div>
</div>

<section class="panel" style="left:96px;top:600px">
  <h2><em>Welcome To</em> VÍKURPRENT</h2>
  <p>Lorem ipsum dolor sit amet, consectetuer amet in adipiscing elit, sed diam nonummy nibh euismod tincidunt ut laoreet dolore magna aliquam erat vol.</p>
  <p>Ut wisi enim ad minim veniam, quis nostrud exerci tation ullamcorper suscipit lobortis nisl ut aliquip commodo consequat.</p>
  <a class="more" href="#">More +</a>
</section>

<section class="panel" style="left:433px;top:600px">
  <h2 class="green"><em>Our</em> Services</h2>
  <p>Lorem ipsum dolor sit amet, consectetuer sed da adipiscing elit, sed diam nonummy nibh euismod tincidunt ut</p>
  <ul class="twocol">
    <li>Lorem ipsum dolor sit</li><li>Lorem ipsum dolor sit</li>
    <li>Lorem ipsum dolor sit</li><li>Lorem ipsum dolor sit</li>
    <li>Lorem ipsum dolor sit</li><li>Lorem ipsum dolor sit</li>
  </ul>
</section>

<section class="panel" style="left:757px;top:600px">
  <h2 class="gold"><em>Easy</em> online graphic editor</h2>
  <div class="editor-shot" role="img" aria-label="Screenshot of the online graphic editor"></div>
</section>

<div class="divider"></div>

<section class="panel" style="left:96px;top:822px">
  <h2><em>Testimonials</em></h2>
  <span class="pager"><i></i><i></i></span>
  <p class="quote">Lorem ipsum dolor sit amet,ctetuer adipiscing elit, sed diam nonummy nibh euismod tincidunt ut laoreet dolore magna aliquam erat volutpat. Ut wisi enim ad minim veniam, quis nostrud ex.</p>
  <p class="author">feugait nulla facilisi.</p>
  <div class="portrait" role="img" aria-label="Portrait photo of the customer"></div>
</section>

<section class="panel" style="left:434px;top:822px">
  <h2 class="green"><em>Advantages</em></h2>
  <ul class="arrows">
    <li>Lorem ipsum dolor sit amet, consectetuer  amet</li>
    <li>Adipiscing elit, sed diam nonummy nibh euismod</li>
    <li>Tincidunt ut laoree dolore magna aliquam eratirei</li>
    <li>Volutpat Ut wisi enim ad minim veniam quistion</li>
    <li>Nostrud exerci tation ullamco suscipit lobortisnis</li>
    <li>Ut aliquip ex ea commodo consequat duis autei</li>
  </ul>
</section>

<section class="panel" style="left:757px;top:822px">
  <h2 class="gold"><em>FAQ's</em></h2>
  <ul class="faq">
    <li>Lorem ipsum dolor sit amet, consectetuer  amet</li>
    <li>Adipiscing elit, sed diam nonummy nibh euismod</li>
    <li>Tincidunt ut laoree dolore magna aliquam eratirei</li>
    <li>Volutpat Ut wisi enim ad minim veniam quistion</li>
    <li>Nostrud exerci tation ullamco suscipit lobortisnis</li>
    <li>Ut aliquip ex ea commodo consequat duis autei</li>
  </ul>
</section>

<footer class="site-footer">
  <div class="fcol" style="left:116px;width:110px">
    <h3>Quick Link</h3>
    <ul><li>Home</li><li>Services &amp; Pricing</li><li>About Us</li><li>Info</li><li>Contact</li></ul>
  </div>
  <div class="fsep" style="left:268px"></div>
  <div class="fcol contact" style="left:312px;width:247px">
    <h3>Contact Us</h3>
    <ul>
      <li><svg width="26" height="22" viewBox="0 0 26 22"><path d="M2 11L13 2l11 9M6 9v11h5v-6h4v6h5V9" fill="none" stroke="#ddd" stroke-width="2.5"/></svg><span>Lorem ipsum dolor sit amet, euismodrit tincidunt ut laoreet dolore my</span></li>
      <li><svg width="26" height="20" viewBox="0 0 26 20"><path d="M6 2c-2 2-2 6 2 11s8 6 10 5l1-3-3-2-2 2c-2-1-4-4-5-6l2-2-2-4z" fill="#ddd"/></svg><span>1300 555 019</span></li>
      <li><svg width="26" height="16" viewBox="0 0 26 16"><rect x="3" y="2" width="20" height="12" fill="none" stroke="#ddd" stroke-width="2"/><path d="M3 2l10 7 10-7" fill="none" stroke="#ddd" stroke-width="2"/></svg><span>info@example.com</span></li>
    </ul>
  </div>
  <div class="fsep" style="left:601px"></div>
  <div class="fcol social" style="left:648px;width:96px">
    <h3>Follow Us</h3>
    <ul><li><i></i>Pagebook</li><li><i></i>Chirper</li><li><i></i>Linkwork</li></ul>
  </div>
  <div class="fsep" style="left:782px"></div>
  <div class="fbrand"><i></i>VÍKURPRENT</div>
  <p class="copy">2013 © vikurprent.example</p>
</footer>

</body>
</html>
```